Halloway Crest Backers Guild business cards

Create a single-sided business card for the Halloway Crest Backers Guild based on the attached logo.
The additional data fields include Name, Title, Email, Phone, and website.
Please use the following as sample data:
Name: Dean Varrow
Title: Co-Founder / Investor
Email: deanvarrow@mailtern.net
Phone: 555-314-2706
Website: www.hcbackersguild.com

Target Market(s)

Start ups, entrepreneurs, venture capitalists

Industry/Entity Type

Investment

Contact Information for Business Card

Professional business card. Technology company.

Font styles to use
Serif
Sans Serif

Requirements
Must have
• Include the HCBG logo (attached)
• Name
• Title
• Email
• Phone
• Website
Should not have
• Cute, cartoony

```html
<!DOCTYPE html>
<html lang="en">
<head>
<meta charset="utf-8">
<title>Halloway Crest Backers Guild – Business Card</title>
<link href="https://fonts.googleapis.com/css2?family=Open+Sans:wght@400;600;700&display=swap" rel="stylesheet">
<style>
  :root {
    --stage: #3b3b3b;
    --card-dark: #131313;
    --brand-green: #2a9448;
    --brand-green-text: #2e9a4a;
    --ink-light: #ffffff;
    --texture: #262626;
  }
  * { margin: 0; padding: 0; box-sizing: border-box; }
  html, body {
    width: 1200px; height: 900px; overflow: hidden;
    background: radial-gradient(circle at 50% 40%, #5a5a5a 0%, var(--stage) 70%);
    font-family: "Open Sans", Arial, sans-serif;
  }
  .stage {
    width: 1200px; height: 900px;
    display: flex; align-items: center; justify-content: center;
  }
  .business-card {
    position: relative;
    width: 1000px; height: 572px;
    background: var(--card-dark);
    overflow: hidden;
    box-shadow: 0 20px 50px rgba(0,0,0,.5);
  }
  .texture-patch {
    position: absolute;
    border-radius: 50%;
    background: radial-gradient(circle, var(--texture) 0%, rgba(38,38,38,0) 70%);
  }
  .texture-patch.left { left: -40px; top: 220px; width: 230px; height: 150px; }
  .texture-patch.right { right: -40px; top: -30px; width: 230px; height: 180px; }
  .brand {
    position: absolute; left: 0; right: 0; top: 150px;
    text-align: center;
    color: var(--brand-green-text);
    font-weight: 400;
    font-size: 44px;
    letter-spacing: 1px;
  }
  .divider-rule {
    position: absolute; left: 0; right: 0; top: 312px;
    height: 6px; background: var(--ink-light);
  }
  .info-band {
    position: absolute; left: 0; right: 0; top: 322px; bottom: 0;
    background: var(--brand-green);
  }
  .identity {
    position: absolute; right: 560px; top: 78px;
    text-align: right; color: var(--ink-light);
    text-transform: uppercase;
  }
  .identity .name { font-weight: 700; font-size: 36px; line-height: 1.1; }
  .identity .title { font-weight: 400; font-size: 22px; }
  .column-rule {
    position: absolute; left: 465px; top: 30px; width: 1px; height: 180px;
    background: rgba(255,255,255,.55);
  }
  .contacts {
    position: absolute; left: 510px; top: 52px;
    list-style: none; color: var(--ink-light);
    font-size: 21px;
  }
  .contacts li { display: flex; align-items: center; height: 38px; }
  .contacts svg { width: 22px; height: 22px; margin-right: 24px; flex: none; }
</style>
</head>
<body>
<main class="stage">
  <article class="business-card">
    <div class="texture-patch left" role="img" aria-label="Subtle dot texture"></div>
    <div class="texture-patch right" role="img" aria-label="Subtle dot texture"></div>

    <h1 class="brand">Halloway Crest Backers Guild</h1>

    <div class="divider-rule"></div>

    <section class="info-band">
      <div class="identity">
        <p class="name">Dean Varrow</p>
        <p class="title">Co-Founder/Investor</p>
      </div>
      <div class="column-rule"></div>
      <ul class="contacts">
        <li>
          <svg viewBox="0 0 24 24" aria-hidden="true"><path fill="#fff" d="M6.6 10.8c1.4 2.8 3.8 5.1 6.6 6.6l2.2-2.2c.3-.3.7-.4 1-.2 1.1.4 2.3.6 3.6.6.6 0 1 .4 1 1V20c0 .6-.4 1-1 1C10.6 21 3 13.4 3 4c0-.6.4-1 1-1h3.5c.6 0 1 .4 1 1 0 1.3.2 2.5.6 3.6.1.3 0 .7-.2 1L6.6 10.8z"/></svg>
          555-314-2706
        </li>
        <li>
          <svg viewBox="0 0 24 24" aria-hidden="true"><rect x="2" y="5" width="20" height="14" fill="#fff"/><path d="M2 5l10 8 10-8M2 19l7-7M22 19l-7-7" stroke="#2a9448" stroke-width="1.6" fill="none"/></svg>
          deanvarrow@mailtern.net
        </li>
        <li>
          <svg viewBox="0 0 24 24" aria-hidden="true"><g fill="none" stroke="#fff" stroke-width="1.6"><circle cx="12" cy="12" r="9"/><ellipse cx="12" cy="12" rx="4" ry="9"/><path d="M3 12h18M5 7h14M5 17h14"/></g></svg>
          www.hcbackersguild.com
        </li>
      </ul>
    </section>
  </article>
</main>
</body>
</html>
```